Food packaging label design

The product name Crisplets, a thin, crispy, and delicious biscuit/cookie made from simple, all natural ingredients. Its name comes from the fact that it looks and tastes a lot like a biscotti cookie, but thinly sliced and much crispier and more delicious than a biscotti. There are currently two flavors: Pure Harvest, and Maple Orchard.

I am looking for a fresh, eye catchy design to go on the label for a rice paper stand up pouch (pouch sample attached). Label size are as follows:

4 oz bag - Width X Height
top: 4.5" x 3.5" bottom: 4.5" x 1.5"

12 oz bag
top: 6.5" x 5.5" bottom: 6.5" x 1.5"

I would like for the top portion of the packaging to include:

Crisplets name
Tag line " a thinner, crispier, and more delicious cousin to the biscotti"
simple and natural ingredients

bottom to include:
net weight
ingredients: wheat flour, eggs, sugar, almonds

Attached is a copy of something I created in powerpoint. you can recreate this using graphic designer software per label specs and improve on it or supprise me with something totally awesome. The key is that it that the colors and design needs to pop or contrast against the white rice paper bag and design needs to be eye catchy, fun and whimsical.

Please refer to link below for best practices for creating artwork for labels to ensure correct format for printing.
http://www.printwellmark.example/label-articles/best-practices-designing-custom-labels/

Good luck!
Updates

Target Market(s)

educated, health conscious consumers such as customers who shops at green basket, brewhollow, market pennys

Industry/Entity Type

Graphic Designer

Requirements
Should not have
• busy or clutter design

```html
<!DOCTYPE html>
<html lang="en">
<head>
<meta charset="utf-8">
<title>Crisplets – pouch labels</title>
<link rel="stylesheet" href="https://fonts.googleapis.com/css2?family=Courgette&family=Itim&family=Kalam:wght@400&display=swap">
<style>
  :root{
    --backdrop:#e4e4e6;
    --label:#ffffff;
    --gold:#e3a21c;
    --cocoa:#7a4a1c;
    --berry:#d6405e;
    --leaf:#6aa23a;
    --ink-brown:#8a4a2a;
    --crisp-light:#efe6c8;
    --crisp-dark:#c9b27a;
  }
  *{box-sizing:border-box;margin:0;padding:0}
  html,body{width:1200px;height:1200px;overflow:hidden}
  body{
    background:radial-gradient(ellipse at 50% 40%, #f2f2f3 0%, var(--backdrop) 75%);
    display:flex;align-items:center;justify-content:center;gap:60px;
    font-family:"Itim",sans-serif;
  }
  .label{
    width:500px;height:1040px;background:var(--label);
    border-radius:14px;box-shadow:0 6px 24px rgba(0,0,0,.12);
    display:flex;flex-direction:column;align-items:center;
    padding:56px 30px 44px;text-align:center;
  }
  .brand-name{
    font-family:"Courgette",cursive;font-size:92px;line-height:1.1;color:var(--gold);
  }
  .tagline{font-size:27px;line-height:1.25;color:var(--ink-brown);margin-top:18px}
  .flavor{font-family:"Courgette",cursive;font-size:48px;font-weight:400;margin-top:14px}
  .flavor--harvest{color:var(--cocoa)}
  .flavor--maple{color:var(--berry)}
  .claim{font-size:30px;color:var(--leaf);margin-top:10px}
  .window{
    width:100%;flex:1 1 auto;margin:22px 0 30px;border-radius:6px;
    background:linear-gradient(135deg,var(--crisp-light) 0%,var(--crisp-dark) 50%,var(--crisp-light) 100%);
  }
  .bottom{display:flex;flex-direction:column;align-items:center;gap:8px;width:100%}
  .ingredients{font-family:"Kalam",cursive;font-size:25px;line-height:1.25;color:var(--ink-brown)}
  .net-weight{font-family:"Kalam",cursive;font-size:34px;color:var(--leaf)}
</style>
</head>
<body>

  <section class="label label--harvest">
    <h1 class="brand-name">Crisplets</h1>
    <p class="tagline">a thinner, crispier, and more delicious<br>cousin to the biscotti</p>
    <h2 class="flavor flavor--harvest">Pure Harvest</h2>
    <p class="claim">simple and natural ingredients</p>
    <div class="window" role="img" aria-label="Clear window showing thin, crisp almond-studded biscuit slices"></div>
    <div class="bottom">
      <p class="ingredients">ingredients:<br>wheat flour, eggs, sugar, almonds</p>
      <p class="net-weight">Net Wt 6 oz</p>
    </div>
  </section>

  <section class="label label--maple">
    <h1 class="brand-name">Crisplets</h1>
    <p class="tagline">a thinner, crispier, and more delicious<br>cousin to the biscotti</p>
    <h2 class="flavor flavor--maple">Maple Orchard</h2>
    <p class="claim">simple and natural ingredients</p>
    <div class="window" role="img" aria-label="Clear window showing thin, crisp biscuit slices with almonds and cranberries"></div>
    <div class="bottom">
      <p class="ingredients">ingredients: wheat flour, eggs, sugar,<br>almonds, cranberries</p>
      <p class="net-weight">Net Wt 12 oz</p>
    </div>
  </section>

</body>
</html>
```